Book cover for publishing doctoral research about various national styles of piano playing.

I need a book cover for a publication of a doctoral research with regard to styles of piano performance characteristic to various nations.

Any images or graphics are optional, typography seems most important, but please feel free to be creative.

I attach the barcode, qsr and publisher's logo in the next few days. (Logo is still being designed).

For various reasons the size of the book is not completely decided yet. Please create your design in 7" x 10", but if at all possible, I would like to ask for files of two sizes, also including 8.5" x 11" in the final submission.

I am looking for a design that looks professional, probably simple, but I am open to any suggestions.

Dear Designers,I would like to thank you all for participation and submitting so many high-quality designs.My final decision was based on the feedback I received from my professional colleagues and potential readers.I would like to wish you all the best for the future.Best wishes,Tadeusz Added Monday, December 21, 2015

Pianists, students, music professionals

Publishing

• Title: Unfolding Seven Harbour Lullabies
• Subtitle: Memories and departures
• Author: Tadeusz Jarocki
• Space for my logo on the front page and the spine.
• On the back page, please include some space for a short biography, 'barcode' and 'qsr' code.
• Please include whatever else you consider necessary.
• Would it be possible to use the same cover to a e-book edition?

```html
<!DOCTYPE html>
<html lang="en">
<head>
<meta charset="utf-8">
<title>Unfolding Seven Harbour Lullabies — Tadeusz Jarocki</title>
<link rel="stylesheet" href="https://fonts.googleapis.com/css2?family=Yanone+Kaffeesatz:wght@300;400&family=Quicksand:wght@600&display=swap">
<style>
  :root {
    --sky-top: #e2bdb1;
    --sky-glow: #fdf4ec;
    --sky-warm: #f0d3bd;
    --stage-light: #f6d49a;
    --stage-gold: #d9a560;
    --stage-mid: #b9803f;
    --stage-deep: #7a4a1e;
    --stage-floor: #2e1b0b;
    --band: #050404;
    --ink-brown: #3a1d1b;
    --ink-plum: #6b2c63;
    --ink-violet: #4a2f7a;
    --subtitle: #a8784c;
    --author: #f6ee7a;
    --logo-line: #a88856;
    --staff: rgba(120, 90, 80, 0.3);
  }
  html, body {
    margin: 0;
    padding: 0;
    overflow: hidden;
    background: #ffffff;
  }
  .cover {
    position: relative;
    width: 849px;
    height: 1200px;
    overflow: hidden;
    background:
      radial-gradient(ellipse 440px 320px at 440px 420px, var(--sky-glow) 0%, rgba(253,244,236,0.6) 45%, rgba(253,244,236,0) 100%),
      linear-gradient(180deg, var(--sky-top) 0%, var(--sky-warm) 40%, #eac69e 55%, var(--stage-gold) 68%);
  }
  .crest {
    position: absolute;
    left: 220px;
    top: -30px;
    width: 410px;
    height: 240px;
    background: radial-gradient(closest-side, #fffaf2 0%, #f7ebdd 40%, rgba(240,222,205,0.55) 70%, rgba(240,222,205,0) 100%);
  }
  .stage {
    position: absolute;
    left: 0;
    top: 540px;
    width: 849px;
    height: 492px;
    background:
      radial-gradient(ellipse 330px 260px at 420px 330px, rgba(252,222,160,0.9) 0%, rgba(246,205,140,0.5) 50%, rgba(246,205,140,0) 100%),
      radial-gradient(ellipse 180px 420px at 0px 280px, rgba(122,74,30,0.55) 0%, rgba(122,74,30,0) 100%),
      radial-gradient(ellipse 180px 420px at 849px 280px, rgba(122,74,30,0.55) 0%, rgba(122,74,30,0) 100%),
      linear-gradient(180deg, rgba(217,165,96,0) 0%, var(--stage-gold) 14%, #d49b55 50%, var(--stage-mid) 76%, var(--stage-deep) 86%, #5a3514 92%, var(--stage-floor) 100%);
  }
  .title-art {
    position: absolute;
    left: 0;
    top: 0;
    width: 849px;
    height: 700px;
  }
  .title-line {
    font-family: "Yanone Kaffeesatz", sans-serif;
    font-weight: 300;
  }
  .subtitle {
    font-family: "Yanone Kaffeesatz", sans-serif;
    font-weight: 300;
    fill: var(--subtitle);
  }
  .footer-band {
    position: absolute;
    left: 0;
    top: 1032px;
    width: 849px;
    height: 168px;
    background:
      radial-gradient(ellipse 300px 10px at 424px 168px, rgba(214,176,110,0.8) 0%, rgba(214,176,110,0) 100%),
      linear-gradient(180deg, #1a120b 0%, var(--band) 16%, var(--band) 100%);
  }
  .author {
    position: absolute;
    left: 150px;
    top: 1082px;
    width: 556px;
    margin: 0;
    text-align: center;
    font-family: "Quicksand", sans-serif;
    font-weight: 600;
    font-size: 44px;
    letter-spacing: 1px;
    line-height: 56px;
    color: var(--author);
  }
  .imprint {
    position: absolute;
    left: 704px;
    top: 1054px;
    width: 86px;
    height: 114px;
    display: flex;
    flex-direction: column;
    align-items: center;
    justify-content: center;
    gap: 8px;
  }
  .imprint-mark {
    width: 58px;
    height: 70px;
    border: 2px solid var(--logo-line);
  }
  .imprint-name {
    font-family: "Quicksand", sans-serif;
    font-weight: 600;
    font-size: 10px;
    letter-spacing: 1px;
    line-height: 12px;
    text-align: center;
    color: var(--logo-line);
  }
</style>
</head>
<body>
<main class="cover">
  <div class="crest" role="img" aria-label="Pearl-white baroque flourish ornament at the top centre"></div>

  <div class="stage" role="img" aria-label="Concert stage with golden curtain and a grand piano with bench under a spotlight"></div>

  <svg class="title-art" width="849" height="700" viewBox="0 0 849 700" aria-label="Unfolding Seven Harbour Lullabies — Memories and departures">
    <defs>
      <linearGradient id="title-ink" x1="0" y1="0" x2="1" y2="0.3">
        <stop offset="0" stop-color="var(--ink-brown)"/>
        <stop offset="0.45" stop-color="var(--ink-plum)"/>
        <stop offset="0.7" stop-color="var(--ink-violet)"/>
        <stop offset="1" stop-color="var(--ink-brown)"/>
      </linearGradient>
    </defs>
    <g class="staff" stroke="var(--staff)" stroke-width="1">
      <line x1="0" y1="314" x2="849" y2="316"/>
      <line x1="0" y1="324" x2="849" y2="326"/>
      <line x1="0" y1="334" x2="849" y2="336"/>
      <line x1="0" y1="344" x2="849" y2="346"/>
      <line x1="0" y1="354" x2="849" y2="356"/>
      <line x1="0" y1="432" x2="849" y2="434"/>
      <line x1="0" y1="442" x2="849" y2="444"/>
      <line x1="0" y1="452" x2="849" y2="454"/>
      <line x1="0" y1="462" x2="849" y2="464"/>
      <line x1="0" y1="472" x2="849" y2="474"/>
    </g>
    <text class="title-line" x="240" y="356" font-size="124" textLength="402" lengthAdjust="spacingAndGlyphs" fill="url(#title-ink)">UNFOLDING</text>
    <text class="title-line" x="240" y="468" font-size="124" textLength="408" lengthAdjust="spacingAndGlyphs" fill="url(#title-ink)">SEVEN</text>
    <text class="title-line" x="68" y="582" font-size="124" textLength="724" lengthAdjust="spacingAndGlyphs" fill="url(#title-ink)">HARBOUR LULLABIES</text>
    <text class="subtitle" x="116" y="650" font-size="60" textLength="626" lengthAdjust="spacingAndGlyphs">MEMORIES AND DEPARTURES</text>
  </svg>

  <div class="footer-band"></div>
  <p class="author">Tadeusz Jarocki</p>

  <div class="imprint">
    <div class="imprint-mark"></div>
    <div class="imprint-name">LARKFIELD<br>BOOKS</div>
  </div>
</main>
</body>
</html>
```